Online Advice via Video Site requires Cutting Edge Homepage

We need a creative new and exciting webdesign for our tutoring via video-chat website.

We have prepared a "demo" homepage for you to see various promotional material that we think would be suitable for the homepage. http://www.quizlanterna.com/demo

The actual site is undergoing some final tinkering but can be accessed and used at http://www.quizlanterna.com

There is NO NEED to take any colours or design structure from this.

We expect the logo to be changed to match the new site. The new logo should match the site's function.

I have included some other projects that we like the look of:
http://www.artflockly.com.au/design/143762
http://www.artflockly.com.au/design/561630
http://www.artflockly.com.au/design/247199
http://www.artflockly.com.au/design/255195
http://www.bravolumo.tv/

Target Market(s)

People that will work as tutors/advisers or be student/clients

Industry/Entity Type

Tutoring

Requirements
Must have
• The search is the main feature of the homepage

After the search the next goal of the page is to get people to sign up to the site

Login, (optional inclusion of the chatterbox login - if you don't include it then you need only have a "login" button... no username or password input fields)

Footer
Nice to have
• The promotional material for the site, the colours on the Slidora file CAN BE changed to suit the new design you propose.

```html
<!DOCTYPE html>
<html lang="en">
<head>
<meta charset="utf-8">
<title>Quiz Lanterna – Homepage</title>
<link href="https://fonts.googleapis.com/css2?family=Open+Sans:wght@300;400;600;700&family=Oswald:wght@400&family=Dancing+Script:wght@500&display=swap" rel="stylesheet">
<style>
:root{
  --ink:#333;
  --muted:#7a7a7a;
  --brand:#2f4fb0;
  --nav-top:#3a5aa8;
  --nav-bottom:#1b3680;
  --green-top:#8cbf1e;
  --green-bottom:#5c8c06;
  --green-text:#7aa815;
  --line:#444;
  --dash:#9a9a9a;
  --dark-btn:#333;
  --teal-a:#a9dcdc;
  --teal-b:#5fb9b9;
  --video:#0d0d0d;
  --player:#1e1e1e;
}
*{box-sizing:border-box;margin:0;padding:0}
html,body{width:1017px;height:1200px;overflow:hidden;background:#fff}
body{font-family:'Open Sans',sans-serif;color:var(--ink);position:relative}
.page{position:absolute;left:8px;top:0;width:1000px;height:1200px}
.abs{position:absolute}

.brand{left:26px;top:36px;font-size:38px;font-weight:300;color:var(--brand);letter-spacing:-0.5px}
.social{left:875px;top:13px;display:flex;gap:4px}
.social span{width:34px;height:34px;border-radius:50%;display:block}
.social .s1{background:#2a4a9a}.social .s2{background:#3fa9dd}.social .s3{background:#d8d8d8}

.login input{position:absolute;top:68px;width:137px;height:25px;border:1px solid #bbb;font:10px 'Open Sans',sans-serif;color:#aaa;padding-left:6px}
.login .user{left:650px}.login .pass{left:793px}
.signin{left:934px;top:67px;width:55px;height:27px;border-radius:6px;background:var(--dark-btn);color:#fff;font-size:11px;font-weight:700;display:flex;align-items:center;justify-content:center;letter-spacing:.3px}
.login-note{top:96px;font-size:10px;color:#333}
.login-note b{color:var(--brand)}

.nav{left:0;top:116px;width:1000px;height:52px;background:linear-gradient(var(--nav-top),var(--nav-bottom));display:flex;align-items:center}
.nav a{color:#fff;text-decoration:none;font-size:15px;padding:0 18px;border-right:1px solid rgba(255,255,255,.35);line-height:30px}
.nav a:first-child{padding-left:29px}
.nav a:last-child{border-right:none}

.search{left:29px;top:183px;width:516px;height:40px;border:1px solid #555;font-size:15px;color:#999;padding:9px 11px}
.category{left:550px;top:186px;width:224px;height:33px;border:1px solid #555;font-size:15px;color:#999;padding:5px 4px}
.category .arrow{position:absolute;right:0;top:0;width:34px;height:31px;border-left:1px solid #555;display:flex;align-items:center;justify-content:center}
.search-btn{left:777px;top:184px;width:197px;height:36px;border-radius:18px;background:linear-gradient(var(--green-top),var(--green-bottom));color:#fff;font-size:15px;display:flex;align-items:center;justify-content:center}

.box{border:1px solid var(--line);background:#fff}
.box h2{font-family:'Oswald',sans-serif;font-weight:400;font-size:19px;text-align:center;height:42px;line-height:42px;border-bottom:1px solid var(--line);letter-spacing:.3px}
.topics{left:29px;top:238px;width:234px;height:310px}
.topics ul{list-style:none;padding-top:5px}
.topics li{height:36px;line-height:36px;font-size:13px;padding-left:47px;border-bottom:1px dashed var(--dash);position:relative}
.topics li:last-child{border-bottom:none}
.topics li::before,.welcome li::before{content:"→";position:absolute;font-size:9px;color:#555}
.topics li::before{left:26px}

.hero{left:277px;top:238px;width:695px;height:310px;border:1px solid #3a8a8a;background:linear-gradient(90deg,var(--teal-a),var(--teal-b))}
.hero .art{position:absolute;left:0;top:0;width:260px;height:308px;background:linear-gradient(160deg,#bfe6e6,#8ccfcf)}
.hero blockquote{position:absolute;left:270px;top:58px;width:400px;text-align:center;font-family:'Dancing Script',cursive;font-size:30px;line-height:49px;color:#fff}
.hero blockquote em{font-style:normal;color:#111}

.contact{left:29px;top:562px;width:234px;height:240px}
.contact h2{color:var(--green-text)}
.field{position:absolute;left:9px;font-size:13px}
.input{position:absolute;left:69px;width:155px;border:1px solid var(--line)}
.send{right:7px;bottom:6px;width:72px;height:26px;border-radius:13px;background:var(--dark-btn);color:#fff;font-family:'Oswald',sans-serif;font-size:15px;display:flex;align-items:center;justify-content:center}

.heading{font-family:'Oswald',sans-serif;font-size:20px;font-weight:400;color:#333}
.heading span{color:var(--brand)}
.welcome{left:345px;top:612px;list-style:none}
.welcome li{position:relative;padding-left:30px;font-size:14px;color:var(--muted);height:35px}
.welcome li::before{left:6px;top:2px}

.video{width:327px;height:280px;background:var(--video)}
.video .bar{position:absolute;left:0;top:0;width:100%;height:30px;background:rgba(40,40,40,.9);color:#fff;font-size:13px;padding:5px 12px}
.video .bar small{position:absolute;top:8px;font-size:10px}
.video .frame{position:absolute;left:0;top:30px;width:100%;height:220px}
.video .play{position:absolute;left:134px;top:110px;width:58px;height:34px;border-radius:6px;background:rgba(30,30,30,.8);border:1px solid #777}
.video .controls{position:absolute;left:0;bottom:0;width:100%;height:30px;background:var(--player);color:#ddd;font-size:10px}

.blog{left:29px;top:816px;width:234px;height:274px}
.blog ul{list-style:none}
.blog li{font-size:12px;line-height:17px;padding:7px 14px 8px 27px;border-bottom:1px dashed var(--dash)}
.blog li:last-child{border-bottom:none}

.footer-line{left:0;top:1104px;width:1000px;border-top:1px solid #999}
.footer-links{left:0;top:1114px;width:970px;text-align:center;font-size:12px;color:#666}
.copyright{left:0;top:1151px;width:970px;text-align:center;font-size:11px;color:#666}
</style>
</head>
<body>
<div class="page">

  <header>
    <div class="abs brand">Quiz Lanterna</div>
    <div class="abs social" aria-label="Social links">
      <span class="s1" title="Chatterbox"></span><span class="s2" title="Chirpline"></span><span class="s3" title="Vidreel"></span>
    </div>
    <form class="login">
      <input class="user" value="Username" aria-label="Username">
      <input class="pass" value="Password" aria-label="Password">
    </form>
    <div class="abs signin">SIGN IN</div>
    <div class="abs login-note" style="left:653px">New User? <b>Register</b></div>
    <div class="abs login-note" style="left:797px">Forgot Password?</div>
  </header>

  <nav class="abs nav">
    <a>Home</a><a>Student</a><a>Advisors</a><a>Topics</a><a>Blog</a><a>FAQs</a><a>Sitemap</a><a>About us</a><a>Our Technology</a><a>Contact</a>
  </nav>

  <div class="abs search">Type Your Search Here......</div>
  <div class="abs category">Categories-------------------
    <div class="arrow"><svg width="16" height="9"><path d="M0 0h16L8 9z" fill="#444"/></svg></div>
  </div>
  <div class="abs search-btn">Search Topics &amp; Advisors</div>

  <aside class="abs box topics">
    <h2>POPULAR TOPICS</h2>
    <ul>
      <li>Health Services</li><li>Hospitality</li><li>Tourism</li><li>Personal Services</li><li>Medical</li><li>Counselling</li><li>Career</li>
    </ul>
  </aside>

  <section class="abs hero">
    <div class="art" role="img" aria-label="Illustration of a thoughtful woman with a chalk thought bubble holding the site name"></div>
    <blockquote>"Imagine if, whenever you had a problem you could instantly access the world's experts to solve it.<br><em>Now you can!</em> "</blockquote>
  </section>

  <aside class="abs box contact">
    <h2>QUICK CONTACT</h2>
    <span class="field" style="top:58px">Name&nbsp;&nbsp;&nbsp;:</span>
    <div class="input" style="top:54px;height:28px"></div>
    <span class="field" style="top:94px">Email&nbsp;&nbsp;&nbsp;&nbsp;:</span>
    <div class="input" style="top:90px;height:27px"></div>
    <span class="field" style="top:130px">Enquiry :</span>
    <div class="input" style="top:124px;height:76px"></div>
    <div class="abs send">SEND</div>
  </aside>

  <h2 class="abs heading" style="left:278px;top:565px">Welcome to Quiz <span>Lanterna</span></h2>
  <ul class="abs welcome">
    <li>QuizLanterna is the place for e-learning, mentoring &amp; professional advice</li>
    <li>It instantly connects people with knowledge and those who need it</li>
    <li>Connects people for ongoing advice or on off answers</li>
    <li>Ask questions and/or work exactly when it suits you</li>
  </ul>

  <h2 class="abs heading" style="left:279px;top:770px">Recent Uploads</h2>

  <div class="abs video" style="left:277px;top:810px">
    <div class="frame" role="img" aria-label="Video still of a presenter gesturing on a dark stage" style="background:linear-gradient(#0a0a14,#1a1a1a)"></div>
    <div class="bar">10 Future Technologi<small style="left:198px">Share</small><small style="left:265px">▼ More info</small></div>
    <div class="play"><svg width="58" height="34"><path d="M23 9l14 8-14 8z" fill="#fff"/></svg></div>
    <div class="controls"><svg width="327" height="30"><circle cx="9" cy="2" r="6" fill="#ccc"/><path d="M24 11l10 6-10 6z" fill="#bbb"/><path d="M66 14h4l5-4v14l-5-4h-4z" fill="#bbb"/><circle cx="227" cy="17" r="5" fill="#bbb"/><path d="M302 10h-4v4M314 10h4v4M302 24h-4v-4M314 24h4v-4" stroke="#bbb" fill="none"/></svg><span class="abs" style="left:100px;top:11px">0:00 / 2:14</span></div>
  </div>

  <div class="abs video" style="left:645px;top:810px">
    <div class="frame" role="img" aria-label="Video still of a man in a hat seated on a chair in a field" style="background:linear-gradient(#8fa3b0 0%,#6a7a70 35%,#4f7a36 55%,#3f6b2a 100%)"></div>
    <div class="bar">Chatterbox Parenting:<small style="left:198px">Share</small><small style="left:265px">▼ More info</small></div>
    <div class="play"><svg width="58" height="34"><path d="M23 9l14 8-14 8z" fill="#fff"/></svg></div>
    <div class="controls"><svg width="327" height="30"><circle cx="9" cy="2" r="6" fill="#ccc"/><path d="M24 11l10 6-10 6z" fill="#bbb"/><path d="M66 14h4l5-4v14l-5-4h-4z" fill="#bbb"/><circle cx="227" cy="17" r="5" fill="#bbb"/><path d="M302 10h-4v4M314 10h4v4M302 24h-4v-4M314 24h4v-4" stroke="#bbb" fill="none"/></svg><span class="abs" style="left:100px;top:11px">0:00 / 8:23</span></div>
  </div>

  <aside class="abs box blog">
    <h2>RECENT BLOG POST</h2>
    <ul>
      <li>How Perfect Should My Site Be Before Launching?</li>
      <li>World’s 20 most powerful busi-ness people 2</li>
      <li>Sample Page</li>
      <li>How Perfect Should My Site Be Before Launching?</li>
      <li>World’s 20 most powerful busi-ness people 2</li>
    </ul>
  </aside>

  <footer>
    <div class="abs footer-line"></div>
    <div class="abs footer-links">Home | Student | Advisors | Topics | Blog | FAQs | Sitemap | About us | Our Technology | Contact</div>
    <div class="abs copyright">Copyright 2012. All Rights Reserved.</div>
  </footer>

</div>
</body>
</html>
```